PROFESSIONAL MODERN REDESIGN OF CURRENT WEBSITE USING ALL SAME CONTENT

I need to redesign existing website using all existing exact content. Please do not leave anything missing. Use all content.

www.brightpathpromotionsgroup.biz

Target Market(s)

Small business owners, business to business, B2B

Industry/Entity Type

Direct Marketing

Number of Pages Required

5+ page

Colors

Designer to choose colors to be used in the design.

Requirements
Must have
• Must use exact same content as www.brightpathpromotionsgroup.biz
Nice to have
• I'd like this to be an easy to read professionally designed website with all modern elements...
Should not have
• Open

```html
<!DOCTYPE html>
<html lang="en">
<head>
<meta charset="utf-8">
<title>BrightPath Promotions Group – Premium Incentive Marketing Services</title>
<link href="https://fonts.googleapis.com/css2?family=Dosis:wght@500;600;700&family=Poppins:wght@300;400;500;600&display=swap" rel="stylesheet">
<style>
:root{
  --orange:#f39a1d;
  --blue:#1672c2;
  --blue-dark:#0f5ea6;
  --cream:#fdefd7;
  --ink:#333333;
  --muted:#666666;
  --soft:#f3f5f8;
  --white:#ffffff;
}
*{box-sizing:border-box;margin:0;padding:0}
html,body{width:1200px;height:3417px;overflow:hidden}
body{font-family:"Poppins",sans-serif;color:var(--ink);background:var(--white);position:relative}
.abs{position:absolute}
.heading{font-family:"Dosis",sans-serif;font-weight:700;color:var(--orange);text-align:center;position:absolute;left:0;width:1200px}
.pill{position:absolute;display:flex;align-items:center;justify-content:center;border-radius:30px;background:var(--blue);color:var(--white);font-family:"Dosis",sans-serif;font-weight:700;font-size:14px;box-shadow:0 6px 12px rgba(22,114,194,.35);text-decoration:none}

/* header */
.site-header{position:absolute;left:0;top:0;width:1200px;height:102px;background:var(--white)}
.brand{position:absolute;left:86px;top:30px;display:flex;align-items:center;gap:10px;font-family:"Dosis",sans-serif;font-weight:700;font-size:24px;color:var(--blue)}
.brand-mark{width:26px;height:26px;background:var(--blue)}
.account-links{position:absolute;left:733px;top:16px;font-size:14px;color:#6a9fd3}
.account-links span{margin-right:30px}
.phone-badge{position:absolute;left:892px;top:8px;width:36px;height:36px;border-radius:50%;background:var(--blue)}
.phone-text{position:absolute;left:943px;top:12px;font-size:10px;line-height:15px;color:var(--ink)}
.header-rule{position:absolute;left:733px;top:53px;width:381px;height:1px;background:#999}
.main-nav{position:absolute;top:68px;left:0;font-size:14px;color:var(--ink)}
.main-nav span{position:absolute;white-space:nowrap}
.main-nav .current{color:var(--blue)}

/* hero */
.hero{position:absolute;left:0;top:102px;width:1200px;height:472px;background:var(--cream)}
.hero-title{position:absolute;left:86px;top:150px;font-family:"Dosis",sans-serif;font-weight:700;font-size:35px;line-height:41px;color:var(--orange)}
.hero-copy{position:absolute;left:86px;top:248px;width:420px;font-family:"Dosis",sans-serif;font-weight:500;font-size:17px;line-height:26px;color:var(--ink)}
.watch{position:absolute;left:318px;top:360px;display:flex;align-items:center;gap:10px;font-family:"Dosis",sans-serif;font-weight:600;font-size:14px}
.hero-photo{position:absolute;left:663px;top:8px;width:345px;height:464px;background:linear-gradient(180deg,#e7d6c4 0%,#6b5047 40%,#1e2a2a 100%);border-radius:160px 160px 0 0}

/* reasons */
.sub{position:absolute;left:0;width:1200px;text-align:center;font-size:12px;color:var(--muted)}
.reason{position:absolute;top:772px;width:170px;text-align:center;font-family:"Dosis",sans-serif;font-weight:500;font-size:16px;line-height:21px;color:var(--ink)}
.reason svg{display:block;margin:0 auto 12px}

/* certificates */
.cert-band{position:absolute;left:0;top:975px;width:1200px;height:1155px;background:linear-gradient(180deg,#fafbfd 0%,#ffffff 25%,#eef1f5 55%,#e7ebef 75%,#ffffff 100%)}
.office-photo{position:absolute;left:0;top:1560px;width:1200px;height:570px;background:linear-gradient(180deg,rgba(210,216,222,.15),rgba(190,198,206,.45) 50%,rgba(230,234,238,.2));}
.cert{position:absolute;top:1168px;width:240px}
.cert-img{height:118px;border-top:3px solid var(--blue)}
.cert-label{height:52px;background:var(--blue);color:var(--white);font-family:"Dosis",sans-serif;font-weight:700;font-size:14px;display:flex;align-items:center;justify-content:center}
.cert-text{margin-top:14px;text-align:center;font-size:11px;line-height:21px;color:var(--ink)}
.cert-text b{color:var(--blue);font-weight:500}
.cert-link{position:absolute;top:268px;left:68px;font-family:"Dosis",sans-serif;font-weight:700;font-size:13px;color:var(--blue);display:flex;align-items:center;gap:18px}

/* plug-in areas */
.area{position:absolute;width:335px;height:127px;background:var(--white);box-shadow:0 2px 8px rgba(0,0,0,.12);display:flex}
.area-img{width:128px;height:127px;flex:none}
.area-body{padding:8px 8px 0 8px}
.area-body h3{font-family:"Dosis",sans-serif;font-weight:600;font-size:14px;line-height:18px;color:var(--ink)}
.area-body p{margin-top:4px;font-size:10px;line-height:17px;color:var(--muted)}

/* distribution */
.distribution{position:absolute;left:0;top:2131px;width:1200px;height:495px;background:var(--blue)}
.step{position:absolute;top:116px;width:240px;text-align:center;color:var(--white)}
.step-ring{width:100px;height:100px;margin:0 auto;border-radius:50%;background:var(--white);border:4px solid var(--orange);display:flex;align-items:center;justify-content:center}
.step h3{margin-top:20px;font-family:"Dosis",sans-serif;font-weight:700;font-size:19px}
.step p{margin-top:12px;font-size:12px;line-height:19px}
.flow-arrow{position:absolute}
.call-btn{position:absolute;left:497px;top:419px;width:206px;height:52px;border-radius:30px;background:var(--white);display:flex;align-items:center;justify-content:center;font-family:"Dosis",sans-serif;font-weight:700;font-size:13px;color:var(--blue)}
.call-btn em{font-style:normal;color:var(--orange);margin:0 3px}

/* materials */
.materials{position:absolute;left:0;top:2626px;width:1200px;height:410px;background:#f2f2f2}
.material{position:absolute;top:176px;width:240px}
.material-img{height:120px}
.material-label{height:52px;background:var(--blue);color:var(--white);font-family:"Dosis",sans-serif;font-weight:700;font-size:19px;display:flex;align-items:center;justify-content:center}

/* start today */
.promo-box{position:absolute;left:227px;top:3097px;width:273px;height:291px;background:linear-gradient(180deg,#1a7fd3,#1670c0);color:var(--white);text-align:center}
.promo-box h3{font-family:"Dosis",sans-serif;font-weight:700;font-size:17px;color:var(--orange);margin-top:16px}
.promo-box p{font-size:13px;line-height:20px;font-weight:500}
.promo-rule{position:absolute;left:24px;width:225px;height:1px;background:rgba(255,255,255,.5)}
.start{position:absolute;left:568px;top:3100px;width:460px}
.start h3{font-family:"Dosis",sans-serif;font-weight:600;font-size:18px;color:var(--ink)}
.start p{margin-top:14px;font-size:13px;line-height:22px;color:var(--muted)}
</style>
</head>
<body>

<header class="site-header">
  <div class="brand"><span class="brand-mark"></span>BrightPath Promotions Group</div>
  <div class="account-links"><span>Log In</span><span>Sign Up</span></div>
  <div class="phone-badge">
    <svg width="36" height="36" viewBox="0 0 36 36"><path d="M13 10c1-1 2-1 3 0l2 3c.6 1 .3 1.8-.5 2.4l-1 .8c.8 2 2.4 3.6 4.4 4.4l.8-1c.6-.8 1.4-1.1 2.4-.5l3 2c1 .8 1 2 0 3l-1.3 1.3C23 27 12 17 11.7 11.3z" fill="#fff"/></svg>
  </div>
  <div class="phone-text">USA Office : 619-555-0142<br>International : 1-800-555-0179</div>
  <div class="header-rule"></div>
  <nav class="main-nav">
    <span style="left:499px">Home</span>
    <span style="left:573px">Our Incentives</span>
    <span style="left:701px">Samples</span>
    <span style="left:793px">Affiliates</span>
    <span style="left:879px">Testimonials</span>
    <span style="left:996px">Faqs</span>
    <span class="current" style="left:1061px">Contact</span>
  </nav>
</header>

<section class="hero">
  <h1 class="hero-title">PREMIUM INCENTIVE<br>MARKETING SERVICES</h1>
  <p class="hero-copy">Boost Sales From Your Existing Marketing Efforts Creating Exciting Promotions With Access To Unlimited Quantity of Our Incentive Certificates</p>
  <a class="pill" style="left:86px;top:351px;width:206px;height:54px">Sign Up For Free 30 day Trial</a>
  <div class="watch">
    <svg width="34" height="34" viewBox="0 0 34 34"><circle cx="17" cy="17" r="15.5" fill="#fff" stroke="#f39a1d" stroke-width="2"/><path d="M13 10l10 7-10 7z" fill="#f39a1d"/></svg>
    Watch Video
  </div>
  <div class="hero-photo" role="img" aria-label="Smiling businesswoman in a dark blazer with arms crossed"></div>
</section>

<h2 class="heading" style="top:668px;font-size:28px">Right Fit And Logical Choice</h2>
<p class="sub" style="top:708px">See How We Are Better Than others</p>

<div class="reason" style="left:77px">
  <svg width="84" height="84" viewBox="0 0 84 84"><path d="M20 10h50l-8 60H12z" fill="#fde3c2"/><rect x="34" y="10" width="28" height="40" fill="none" stroke="#1672c2" stroke-width="3"/><path d="M40 20h16M40 28h16M40 36h10" stroke="#f39a1d" stroke-width="3"/><circle cx="30" cy="44" r="8" fill="none" stroke="#1672c2" stroke-width="3"/><path d="M16 70c0-10 6-16 14-16s14 6 14 16z" fill="none" stroke="#1672c2" stroke-width="3"/></svg>
  14+ Years In<br>Business
</div>
<div class="reason" style="left:204px">
  <svg width="84" height="84" viewBox="0 0 84 84"><path d="M14 20h58l-6 50H18z" fill="#fde3c2"/><g fill="#1672c2"><circle cx="26" cy="30" r="7"/><circle cx="58" cy="30" r="7"/><circle cx="42" cy="44" r="7"/><circle cx="20" cy="50" r="7"/><circle cx="64" cy="50" r="7"/><path d="M30 66c0-8 5-12 12-12s12 4 12 12z"/><path d="M10 70c0-7 4-10 10-10s10 3 10 10z"/><path d="M54 70c0-7 4-10 10-10s10 3 10 10z"/></g><g fill="#f39a1d"><circle cx="42" cy="18" r="6"/></g></svg>
  15,000+ Clients<br>Enrolled
</div>
<div class="reason" style="left:366px">
  <svg width="84" height="84" viewBox="0 0 84 84"><path d="M30 8h40l-6 64H22z" fill="#fde3c2"/><rect x="22" y="8" width="40" height="58" fill="none" stroke="#1672c2" stroke-width="3"/><path d="M30 20h24M30 28h24M30 36h24" stroke="#f39a1d" stroke-width="3"/><circle cx="42" cy="50" r="6" fill="none" stroke="#1672c2" stroke-width="3"/><path d="M38 55l-2 12 6-3 6 3-2-12" fill="none" stroke="#1672c2" stroke-width="3"/></svg>
  4+ Million Certificates<br>Distributed
</div>
<div class="reason" style="left:557px">
  <svg width="84" height="84" viewBox="0 0 84 84"><path d="M14 14h56l-6 58H18z" fill="#fde3c2"/><rect x="16" y="32" width="52" height="12" fill="none" stroke="#1672c2" stroke-width="3"/><rect x="20" y="44" width="44" height="26" fill="none" stroke="#1672c2" stroke-width="3"/><path d="M42 32v38M34 32v38M50 32v38" stroke="#1672c2" stroke-width="3"/><path d="M42 32c-6-12-18-10-14-2M42 32c6-12 18-10 14-2" fill="none" stroke="#1672c2" stroke-width="3"/></svg>
  Hundreds Of Thousands<br>Of Redemptions
</div>
<div class="reason" style="left:745px">
  <svg width="84" height="84" viewBox="0 0 84 84"><path d="M30 6h34l12 40-20 26H24z" fill="#fde3c2"/><circle cx="46" cy="26" r="9" fill="none" stroke="#f39a1d" stroke-width="4" stroke-dasharray="4 3"/><circle cx="46" cy="26" r="3" fill="#1672c2"/><path d="M14 52c10-4 18-4 24 0h14c4 0 4 6 0 6H36M14 64c10 6 26 6 40-4l14-10" fill="none" stroke="#1672c2" stroke-width="3"/></svg>
  Top Notch Customer<br>Service
</div>
<div class="reason" style="left:923px">
  <svg width="84" height="84" viewBox="0 0 84 84"><path d="M40 8h34l-4 64H36z" fill="#fde3c2"/><rect x="12" y="10" width="60" height="46" fill="none" stroke="#1672c2" stroke-width="3"/><path d="M24 22h36M24 30h36M24 38h36" stroke="#f39a1d" stroke-width="3"/><circle cx="42" cy="52" r="7" fill="#fff" stroke="#1672c2" stroke-width="3"/><path d="M37 58l-2 12 7-3 7 3-2-12" fill="#fff" stroke="#1672c2" stroke-width="3"/></svg>
  Licensed Seller Of<br>Travel CST #4417306
</div>

<div class="cert-band"></div>
<div class="office-photo" role="img" aria-label="Blurred office scene with colleagues talking"></div>

<h2 class="heading" style="top:1028px;font-size:29px">Unlimited Amount of Gift certificates</h2>
<p class="sub" style="top:1073px;font-size:11px;line-height:17px">For $99/Mo You CanAttract More Customers By Creating Sxciting Promotional<br>Giveaways Using an unimited amount of certificates redeemable for :</p>

<div class="cert" style="left:93px">
  <div class="cert-img" role="img" aria-label="Airplane flying through a cloudy sky" style="background:linear-gradient(160deg,#5d7f97,#b9c9d4 55%,#6f8797)"></div>
  <div class="cert-label">Vacation Getaway Certificates</div>
  <p class="cert-text">Resort Stays, Cruises &amp; Airfares<br>Up To <b>$3000.00</b> Retail Value Your<br>Customers Just Pay Taxes!</p>
  <div class="cert-link">View Certifications <svg width="24" height="10" viewBox="0 0 24 10"><path d="M0 5h22M17 1l5 4-5 4" fill="none" stroke="#1672c2" stroke-width="1.5"/></svg></div>
</div>
<div class="cert" style="left:350px">
  <div class="cert-img" role="img" aria-label="Restaurant table with plates of fries" style="border-top-color:#f39a1d;background:linear-gradient(160deg,#2b2622,#8a5b2a 50%,#3a302a)"></div>
  <div class="cert-label">Restaurant Gift Certificates</div>
  <p class="cert-text"><b>$25-$300</b> Retail Value<br>Thousands Of Restaurants<br>Nationwide!</p>
  <div class="cert-link">View Certifications <svg width="24" height="10" viewBox="0 0 24 10"><path d="M0 5h22M17 1l5 4-5 4" fill="none" stroke="#1672c2" stroke-width="1.5"/></svg></div>
</div>
<div class="cert" style="left:607px">
  <div class="cert-img" role="img" aria-label="Desk with laptops, tablets and coffee seen from above" style="background:linear-gradient(160deg,#8c8f8a,#c7c3b8 50%,#6d7276)"></div>
  <div class="cert-label">Electronic Product Giveaways</div>
  <p class="cert-text">HD Tablets, Premium Earbuds,<br>Smart Watches, Mp4 Players<br><b>$100-$199</b> Retail Value</p>
  <div class="cert-link">View Certifications <svg width="24" height="10" viewBox="0 0 24 10"><path d="M0 5h22M17 1l5 4-5 4" fill="none" stroke="#1672c2" stroke-width="1.5"/></svg></div>
</div>
<div class="cert" style="left:865px">
  <div class="cert-img" role="img" aria-label="Red neon wine sign lettering" style="border-top-color:#f39a1d;background:linear-gradient(90deg,#3a0608,#c8141c 30%,#4a0a0c 55%,#b31218 80%,#2c0506)"></div>
  <div class="cert-label">Gas, Grocery &amp; Wine Vouchers</div>
  <p class="cert-text">Available In <b>$50-$100</b><br>Denomination</p>
  <div class="cert-link">View Certifications <svg width="24" height="10" viewBox="0 0 24 10"><path d="M0 5h22M17 1l5 4-5 4" fill="none" stroke="#1672c2" stroke-width="1.5"/></svg></div>
</div>

<a class="pill" style="left:497px;top:1484px;width:206px;height:52px">Get A 100% Free Sample Package</a>

<h2 class="heading" style="top:1626px;font-size:29px">We Plug Right Into Your Existing advertising In 4 Major areas</h2>

<div class="area" style="left:252px;top:1720px">
  <div class="area-img" role="img" aria-label="Hand moving a chess piece" style="background:linear-gradient(150deg,#1c2a44,#5b6f8f 50%,#1a2236)"></div>
  <div class="area-body"><h3>Boost Response Rates To<br>Your Existing Ads</h3><p>Add a simple tagline to all your ads "Contact us today and receive Two Nights In Las Vegas, No Purchase Necessary!</p></div>
</div>
<div class="area" style="left:613px;top:1720px">
  <div class="area-img" role="img" aria-label="Business handshake between colleagues" style="background:linear-gradient(150deg,#3d3b38,#8d8478 50%,#2e2c2a)"></div>
  <div class="area-body"><h3>Get More New Customers</h3><p>Now that you have generated a new lead go ahead and offer a higher valued incentive like our Airfare Plus Hotel Getaway persuade them to purchase today vs tomorrow!</p></div>
</div>
<div class="area" style="left:252px;top:1892px">
  <div class="area-img" role="img" aria-label="Businessman beside a rising bar chart" style="background:linear-gradient(150deg,#0d1720,#1f6f86 55%,#0a1218)"></div>
  <div class="area-body"><h3>Increase Repeat &amp;<br>Referral Business</h3><p>You have a reason to contact your clients to remind them about your services with a 7 Night Resort Getway to motivate them to buy again!</p></div>
</div>
<div class="area" style="left:613px;top:1892px">
  <div class="area-img" role="img" aria-label="Hand pointing at a tablet with charts" style="background:linear-gradient(150deg,#eef3f8,#b7cde3 55%,#dde6ee)"></div>
  <div class="area-body"><h3>Boost Your Referral Business</h3><p>Offer a $100 Wine Voucher or even our Two Night Bahama Cruise to entice your customers to send you a referral and then watch your referral business soar!</p></div>
</div>

<a class="pill" style="left:497px;top:2061px;width:206px;height:52px">Quick 30 day Free trial Sign Up</a>

<section class="distribution">
  <h2 class="heading" style="top:36px;font-size:29px">Easy Distribution of incentive</h2>

  <svg class="flow-arrow" style="left:262px;top:148px" width="110" height="90" viewBox="0 0 110 90"><path d="M2 4L100 82M88 82h12V70" fill="none" stroke="#f39a1d" stroke-width="1.5" stroke-dasharray="3 3"/></svg>
  <svg class="flow-arrow" style="left:528px;top:132px" width="110" height="90" viewBox="0 0 110 90"><path d="M2 86L100 8M88 8h12v12" fill="none" stroke="#f39a1d" stroke-width="1.5" stroke-dasharray="3 3"/></svg>
  <svg class="flow-arrow" style="left:810px;top:148px" width="110" height="90" viewBox="0 0 110 90"><path d="M2 4L100 82M88 82h12V70" fill="none" stroke="#f39a1d" stroke-width="1.5" stroke-dasharray="3 3"/></svg>

  <div class="step" style="left:70px">
    <div class="step-ring"><svg width="50" height="50" viewBox="0 0 50 50" fill="none" stroke="#f39a1d" stroke-width="2.5"><rect x="14" y="6" width="22" height="12"/><rect x="6" y="18" width="38" height="18" rx="3"/><rect x="14" y="28" width="22" height="16"/><path d="M18 34h14M18 39h14"/></svg></div>
    <h3>Print</h3>
    <p>Download PDF certificates to print and physically hand them out or mail them to your customers.</p>
  </div>
  <div class="step" style="left:332px">
    <div class="step-ring"><svg width="50" height="50" viewBox="0 0 50 50" fill="none" stroke="#f39a1d" stroke-width="2.5"><rect x="6" y="12" width="36" height="26"/><path d="M6 12l18 14 18-14M6 38l13-12M42 38L29 26"/><path d="M34 40h12M42 36l4 4-4 4"/></svg></div>
    <h3>Email</h3>
    <p>Email E-Certificates to your customers individually and in bulk with just one click.</p>
  </div>
  <div class="step" style="left:611px">
    <div class="step-ring"><svg width="56" height="50" viewBox="0 0 56 50" fill="none" stroke="#f39a1d" stroke-width="2.5"><rect x="4" y="14" width="40" height="18" rx="3"/><text x="9" y="27" font-size="9" fill="#f39a1d" stroke="none" font-family="Poppins,sans-serif">http://</text><path d="M36 24l10 20 3-8 8-2z" fill="#fff"/></svg></div>
    <h3>Web Banners or API Integration</h3>
    <p>Install our HTML web banners on the thank you pages of your website to automate distribution of our incentives and if you are tech savvy you can integrate our NEW API too!</p>
  </div>
  <div class="step" style="left:889px">
    <div class="step-ring"><svg width="50" height="50" viewBox="0 0 50 50" fill="none" stroke="#f39a1d" stroke-width="2.5"><path d="M8 8h34a4 4 0 014 4v20a4 4 0 01-4 4H20l-10 8v-8H8a4 4 0 01-4-4V12a4 4 0 014-4z"/><circle cx="16" cy="22" r="2.5"/><circle cx="25" cy="22" r="2.5"/><circle cx="34" cy="22" r="2.5"/></svg></div>
    <h3>SMS/Text Messaging</h3>
    <p>Send certificates through text messaging with just one click with our new SMS feature with no per sms fees!</p>
  </div>

  <div class="call-btn">Click And we will <em>Call</em> You</div>
</section>

<section class="materials">
  <h2 class="heading" style="top:70px;font-size:29px;line-height:31px">Promotional Marketing Materials To Help You<br>Promote The Incentive To Your Customers</h2>

  <div class="material" style="left:93px">
    <div class="material-img" role="img" aria-label="Poster of a city skyline lit up at night" style="background:linear-gradient(160deg,#2a1a3a,#c0552a 45%,#f0b84a 60%,#2a1a3a)"></div>
    <div class="material-label">Posters &amp; Flyers</div>
  </div>
  <div class="material" style="left:350px">
    <div class="material-img" role="img" aria-label="Laptop showing a video player" style="background:linear-gradient(160deg,#f4f4f4,#d8dde3 50%,#b3222a 51%,#e9ecef)"></div>
    <div class="material-label">Web Videos</div>
  </div>
  <div class="material" style="left:607px">
    <div class="material-img" role="img" aria-label="Product description brochure page" style="background:linear-gradient(180deg,#1c5a9c 0 24%,#eef1f5 24%,#dfe5ec)"></div>
    <div class="material-label">Product Description Brochures</div>
  </div>
  <div class="material" style="left:865px">
    <div class="material-img" role="img" aria-label="Marketing tips document page" style="background:linear-gradient(180deg,#1c5a9c 0 24%,#ffffff 24%,#eceff3)"></div>
    <div class="material-label">Tips</div>
  </div>
</section>

<aside class="promo-box">
  <h3>Get Promotional Design Material</h3>
  <p style="position:absolute;left:10px;top:92px;width:253px">You will get Professionally designed Flayers &amp; Posters</p>
  <div class="promo-rule" style="top:150px"></div>
  <p style="position:absolute;left:10px;top:180px;width:253px">You will also Get Professioanl Marketing Tips</p>
  <div class="promo-rule" style="top:240px"></div>
  <p style="position:absolute;left:10px;top:258px;width:253px">and Much More...</p>
</aside>

<div class="start">
  <h3>Start Today</h3>
  <p>We help you by providing full color, professionally designed flyers &amp; posters for each incentive that you can get printed at your local print shop or any online printing company.</p>
  <p style="margin-top:20px">We also provide you with customer appreciation letter templates and warm lead letter templates as well as proven incentive marketing tips and strategies to help you get the most from promotional campaigns.</p>
</div>
<a class="pill" style="left:562px;top:3332px;width:204px;height:52px">Contact Us Direct Today</a>

</body>
</html>
```